Short video intro graphic animation featuring brand mark

I would like a new branded video intro graphic animation to place at the start of the videos I make.
Look at some of the videos on this page for example.
https://www.grovantfield.com/video#!
A more simple one is featured here;
https://www.clipvarno.com/watch?v=Qm7pwrTbN3c
I would like you use white purple and opacity in the graphic.
My logo is simply the text mark in the attachment.
I would like there to be movement as well. It should be quick.
It can include a sound if you like.
The rest is up to you.

```html
<!DOCTYPE html>
<html lang="en">
<head>
<meta charset="UTF-8">
<title>Vimalo – Video Intro Frame</title>
<link rel="stylesheet" href="https://fonts.googleapis.com/css2?family=Arimo:wght@400&display=swap">
<style>
  :root {
    --purple-base: #9e6e9c;
    --purple-deep: #8f5f8e;
    --purple-soft: #c49ec3;
    --glow-white: #ffffff;
    --mark-white: #ffffff;
    --mark-faded: rgba(246, 236, 246, 0.72);
  }
  html, body {
    margin: 0;
    padding: 0;
    width: 1200px;
    height: 670px;
    overflow: hidden;
    background: var(--purple-base);
  }
  .intro-frame {
    position: relative;
    width: 1200px;
    height: 670px;
    overflow: hidden;
    font-family: "Arimo", Arial, sans-serif;
  }
  .wall-texture {
    position: absolute;
    inset: 0;
    background:
      linear-gradient(180deg, var(--purple-soft) 0%, var(--purple-base) 45%, var(--purple-deep) 100%);
  }
  .spot-glow {
    position: absolute;
    inset: 0;
    background: radial-gradient(ellipse 340px 250px at 58% 0%,
      var(--glow-white) 0%, rgba(255,255,255,0.75) 30%, rgba(255,255,255,0.25) 65%, rgba(255,255,255,0) 100%);
  }
  .brand-name {
    position: absolute;
    margin: 0;
    font-weight: 400;
    line-height: 1;
    white-space: nowrap;
    letter-spacing: -0.01em;
  }
  .brand-name--center {
    left: 496px;
    top: 232px;
    font-size: 140px;
    color: var(--mark-white);
  }
  .brand-name--left {
    left: -190px;
    top: 160px;
    font-size: 230px;
    color: var(--mark-faded);
  }
  .brand-name--right {
    left: 932px;
    top: 160px;
    font-size: 270px;
    color: var(--mark-faded);
  }
</style>
</head>
<body>
  <main class="intro-frame">
    <div class="wall-texture" role="img" aria-label="Distressed purple plaster wall texture"></div>
    <div class="spot-glow"></div>
    <p class="brand-name brand-name--left" aria-hidden="true">Vimalo</p>
    <h1 class="brand-name brand-name--center">Vimalo</h1>
    <p class="brand-name brand-name--right" aria-hidden="true">Vimalo</p>
  </main>
</body>
</html>
```